Cargo Van Wrap

Horizontal Directional Drilling company that specializes in Power and Telecommunications and Fiber Optic installation.

Target Market(s)

Future customers

Colors

Designer to choose colors to be used in the design.

Requirements
Must have
• - Must have the P Logo or the complete logo with business name(both options would be nice)
• - HDD is the abbreviation for Horizontal Directional Drilling if it is too long of a word to fit
• - company website address www.brindlecovecontracting.com
• - company slogan somewhere " Experts in Power and Telecommunication construction "
• - company colours are black, orange and silver or gray
Nice to have
• - Something to make the man door on the side standout or look different somehow
• - the cab of the truck to be incorporated someway
Should not have
• non company colours
• phone number

```html
<!DOCTYPE html>
<html lang="en">
<head>
<meta charset="utf-8">
<title>Brindle Cove Contracting – Box Truck Wrap</title>
<link rel="stylesheet" href="https://fonts.googleapis.com/css2?family=Orbitron:wght@700;800&family=Fira+Sans+Extra+Condensed:ital,wght@0,600;1,600&display=swap">
<style>
  :root {
    --stage: #e6e6e6;
    --wrap-deep: #07041a;
    --wrap-navy: #0d0a3a;
    --glow-blue: #2a4dff;
    --glow-cyan: #3fb8ff;
    --glow-magenta: #c42ad8;
    --glow-violet: #6a2bd6;
    --silver-light: #ffffff;
    --silver-mid: #c9d3e6;
    --silver-dark: #8ea0c4;
    --text-white: #ffffff;
    --brand-orange: #e8532a;
  }
  * { box-sizing: border-box; margin: 0; padding: 0; }
  html, body {
    width: 1200px; height: 800px; overflow: hidden;
    background: var(--stage);
  }
  .canvas {
    position: relative; width: 1200px; height: 800px;
  }
  .wrap-panel {
    position: absolute; left: 50px; top: 202px;
    width: 1100px; height: 396px; overflow: hidden;
    background: var(--wrap-deep);
    box-shadow: 0 6px 18px rgba(0,0,0,0.18);
  }
  .tech-artwork {
    position: absolute; inset: 0;
    background:
      radial-gradient(circle at 200px 215px, rgba(63,184,255,0.55) 0, rgba(42,77,255,0.45) 90px, rgba(42,77,255,0) 230px),
      radial-gradient(circle at 330px 180px, rgba(196,42,216,0.75) 0, rgba(106,43,214,0.45) 120px, rgba(106,43,214,0) 280px),
      radial-gradient(ellipse at 560px 200px, rgba(106,43,214,0.35) 0, rgba(13,10,58,0) 360px),
      linear-gradient(90deg, var(--wrap-navy) 0%, var(--wrap-deep) 70%, #05030f 100%);
  }
  .brand-mark {
    position: absolute; left: 43px; top: 40px;
    display: flex; align-items: center; gap: 12px;
  }
  .brand-mark .dot {
    width: 46px; height: 46px; border-radius: 50%;
    background: var(--brand-orange);
  }
  .brand-mark .name {
    font-family: "Fira Sans Extra Condensed", sans-serif;
    font-weight: 600; font-size: 26px; color: var(--text-white);
  }
  .headline {
    position: absolute; right: 22px; top: 36px;
    text-align: right;
    font-family: "Orbitron", sans-serif; font-weight: 800;
    font-size: 44px; line-height: 58px; letter-spacing: 1px;
    background: linear-gradient(180deg, var(--silver-light) 20%, var(--silver-mid) 55%, var(--silver-dark) 100%);
    -webkit-background-clip: text; background-clip: text;
    color: transparent;
    filter: drop-shadow(0 0 6px rgba(63,184,255,0.55));
  }
  .slogan {
    position: absolute; right: 22px; top: 164px;
    text-align: right;
    font-family: "Fira Sans Extra Condensed", sans-serif;
    font-style: italic; font-weight: 600;
    font-size: 33px; line-height: 37px; color: var(--text-white);
  }
  .website {
    position: absolute; right: 24px; top: 320px;
    font-family: "Fira Sans Extra Condensed", sans-serif;
    font-weight: 600; font-size: 32px; letter-spacing: 0.5px;
    color: var(--text-white);
  }
</style>
</head>
<body>
  <main class="canvas">
    <section class="wrap-panel">
      <div class="tech-artwork" role="img" aria-label="Glowing blue and magenta circuit-board rings and data lines radiating across a dark background"></div>
      <div class="brand-mark">
        <span class="dot"></span>
        <span class="name">Brindle Cove Contracting</span>
      </div>
      <h1 class="headline">HORIZONTAL<br>DIRECTIONAL DRILLING</h1>
      <p class="slogan">Experts in Power and Telecommunication<br>construction</p>
      <p class="website">www.brindlecovecontracting.com</p>
    </section>
  </main>
</body>
</html>
```